Tradeline Summit & Fair xmas banner/MREC promotion

Size:
• Leader board: 728 x 90 px
• MREC: 300 x250 px
• Half-page: 300 x 600
• Wide skyscraper: 160 x 600
Image:
Candy cane stripes as the background – image bought. Horizontal or vertical whatever you think will works.
White strip/background for the copy? See images example – unless you don’t need to do that?
Bold font which is "neutra" to our other banners attached. I think black font would look good.
Message:
Please give it a good readable pace between slides – 3 secs?
1st Slide
It’s silly season!
2nd Slide
Treat yourself to an end of year gift
3rd Slide
Book your ticket now and save $$$
4th Slide
Get spoilt. You’re worth it!
5th Slide
Tradeline logo
Target Market(s)
anyone that sells online
• Automotive • Advertising • Digital • Entertainment
• Finance • Hospitality • Pharmaceutical/Healthcare • Pop Culture
• Retail • Travel • Telecommunications

```html
<!DOCTYPE html>
<html lang="en">
<head>
<meta charset="utf-8">
<title>Tradeline Summit &amp; Fair – Xmas Banner Set</title>
<link rel="stylesheet" href="https://fonts.googleapis.com/css2?family=Josefin+Sans:wght@400;700&display=swap">
<style>
  :root {
    --stage: #1b1b1b;
    --frame-red: #ff1a12;
    --frame-glow: rgba(255, 40, 30, 0.75);
    --ink: #0d0d0d;
    --cane-white: #f6f1ee;
    --cane-pink: #e7b3a4;
    --cane-red: #c9705c;
  }
  * { box-sizing: border-box; margin: 0; padding: 0; }
  html, body {
    width: 1200px;
    height: 1000px;
    overflow: hidden;
    background: var(--stage);
  }
  .board {
    position: relative;
    width: 1200px;
    height: 1000px;
    background: var(--stage);
    font-family: "Josefin Sans", "Futura", sans-serif;
  }
  .banner {
    position: absolute;
    border: 3px solid var(--frame-red);
    box-shadow: 0 0 6px 1px var(--frame-glow);
    display: flex;
    align-items: center;
    justify-content: center;
    overflow: hidden;
  }
  .banner-photo {
    position: absolute;
    inset: 0;
    background:
      radial-gradient(ellipse at center, rgba(255,255,255,0.95) 0%, rgba(255,255,255,0.6) 40%, rgba(255,255,255,0) 75%),
      linear-gradient(115deg, var(--cane-pink), var(--cane-white) 30%, var(--cane-pink) 55%, var(--cane-white) 75%, var(--cane-red));
  }
  .leaderboard { left: 48px; width: 730px; height: 91px; }
  .leaderboard .headline { font-size: 27px; }
  .mrec { width: 300px; height: 251px; }
  .headline {
    position: relative;
    color: var(--ink);
    font-weight: 700;
    text-transform: uppercase;
    text-align: center;
    letter-spacing: 0.2px;
    padding-top: 4px;
  }
  .mrec .headline { font-size: 28px; line-height: 37px; }
  .brand {
    position: relative;
    color: var(--ink);
    font-weight: 400;
    text-align: right;
    line-height: 1;
  }
  .brand-name { display: block; font-size: 38px; letter-spacing: 0.5px; }
  .brand-tag { display: block; font-size: 14px; margin-top: 2px; }
  .mrec .brand-name { font-size: 32px; }
  .mrec .brand-tag { font-size: 12px; }
</style>
</head>
<body>
<main class="board">
  <section class="banner leaderboard" style="top:101px">
    <div class="banner-photo" role="img" aria-label="Candy cane stripes photo, softened white in the centre"></div>
    <p class="headline">It’s silly season!</p>
  </section>
  <section class="banner leaderboard" style="top:209px">
    <div class="banner-photo" role="img" aria-label="Candy cane stripes photo, softened white in the centre"></div>
    <p class="headline">Treat yourself to an end of year gift</p>
  </section>
  <section class="banner leaderboard" style="top:318px">
    <div class="banner-photo" role="img" aria-label="Candy cane stripes photo, softened white in the centre"></div>
    <p class="headline">Book your ticket now and save $$$</p>
  </section>
  <section class="banner leaderboard" style="top:425px">
    <div class="banner-photo" role="img" aria-label="Candy cane stripes photo, softened white in the centre"></div>
    <p class="headline">Get spoilt. You’re worth it!</p>
  </section>
  <section class="banner leaderboard" style="top:533px">
    <div class="banner-photo" role="img" aria-label="Candy cane stripes photo, softened white in the centre"></div>
    <p class="brand"><span class="brand-name">Tradeline</span><span class="brand-tag">Summit &amp; Fair</span></p>
  </section>

  <section class="banner mrec" style="left:852px; top:36px">
    <div class="banner-photo" role="img" aria-label="Candy cane stripes photo, softened white in the centre"></div>
    <p class="headline">It’s silly<br>season!</p>
  </section>
  <section class="banner mrec" style="left:852px; top:358px">
    <div class="banner-photo" role="img" aria-label="Candy cane stripes photo, softened white in the centre"></div>
    <p class="headline">Treat<br>yourself to<br>an end of<br>year gift</p>
  </section>
  <section class="banner mrec" style="left:58px; top:680px">
    <div class="banner-photo" role="img" aria-label="Candy cane stripes photo, softened white in the centre"></div>
    <p class="brand"><span class="brand-name">Tradeline</span><span class="brand-tag">Summit &amp; Fair</span></p>
  </section>
  <section class="banner mrec" style="left:455px; top:680px">
    <div class="banner-photo" role="img" aria-label="Candy cane stripes photo, softened white in the centre"></div>
    <p class="headline">Get spoilt.<br>You’re worth it!</p>
  </section>
  <section class="banner mrec" style="left:852px; top:680px">
    <div class="banner-photo" role="img" aria-label="Candy cane stripes photo, softened white in the centre"></div>
    <p class="headline">Book your<br>ticket now<br>and save $$$</p>
  </section>
</main>
</body>
</html>
```